Vantorix Business
Card and Letter Head
Creative Brief
Professional
Dalton Prewitt
Owner
7153 Hollow Creek Christiansted, Port Elsin VI 00947
sales@vantorix.net
vantorix.net
Custom Integrator
ultimate digital experience

```html
<!DOCTYPE html>
<html lang="en">
<head>
<meta charset="utf-8">
<title>Vantorix Stationery</title>
<link href="https://fonts.googleapis.com/css2?family=Open+Sans:wght@400;600;700&display=swap" rel="stylesheet">
<style>
:root{
  --bg:#ececec;
  --paper:#ffffff;
  --ink:#2a2a2a;
  --muted:#7a7a7a;
  --gold:#b8924a;
  --shadow:0 2px 6px rgba(0,0,0,.25);
}
*{box-sizing:border-box;margin:0;padding:0}
html,body{width:1200px;height:499px;overflow:hidden;background:var(--bg);font-family:"Open Sans",Arial,sans-serif;color:var(--ink)}
.canvas{position:relative;width:1200px;height:499px}
.letterhead{position:absolute;top:12px;width:348px;height:478px;background:var(--paper);box-shadow:var(--shadow)}
.letterhead--band{left:12px}
.letterhead--centered{left:382px}
.lh-band{height:56px;background:linear-gradient(#2c2c2c,#151515);display:flex;justify-content:space-between;align-items:flex-start;padding:8px 14px}
.brand{display:flex;align-items:center;gap:5px;font-weight:700;letter-spacing:.08em;text-transform:uppercase;white-space:nowrap}
.brand-dot{border-radius:50%;background:var(--gold);flex:none}
.lh-band .brand{color:#fff;font-size:11px;margin-top:16px}
.lh-band .brand-dot{width:10px;height:10px}
.lh-address{font-size:5px;line-height:1.5;color:#ddd;text-align:right}
.lh-center{text-align:center;padding-top:14px}
.lh-center .brand{justify-content:center;font-size:11px;color:var(--ink)}
.lh-center .brand-dot{width:10px;height:10px}
.lh-center .lh-address{color:var(--muted);text-align:center;margin-top:4px}
.card{position:absolute;width:197px;height:112px;box-shadow:var(--shadow);overflow:hidden;background:var(--paper)}
.card--dark{background:linear-gradient(135deg,#3c3c3c,#161616);color:#eee}
.tagline{position:absolute;left:14px;top:50px;font-size:9px;color:#e8e8e8}
.card-mini{position:absolute;left:14px;bottom:8px;font-size:4px;color:#aaa}
.card--dark .brand{position:absolute;left:0;right:0;top:40px;justify-content:center;font-size:8px;color:#eee}
.card--dark .brand-dot{width:9px;height:9px}
.top-gold{height:22px;background:linear-gradient(#c9a862,#9c7a3a)}
.top-dark{height:22px;background:linear-gradient(#3a3a3a,#151515)}
.bottom-dark{position:absolute;left:0;right:0;bottom:0;height:22px;background:linear-gradient(#3a3a3a,#151515)}
.card .brand.corner{position:absolute;left:10px;top:30px;font-size:8px;color:var(--ink)}
.brand.corner .brand-dot{width:9px;height:9px}
.person{position:absolute;right:12px;top:30px;text-align:right}
.person-name{font-size:7px;font-weight:600;color:var(--gold)}
.person-name--ink{color:var(--ink)}
.person-role{font-size:5px;color:var(--muted)}
.person--large{top:10px}
.person--large .person-name{font-size:10px;color:var(--ink)}
.contact{position:absolute;left:10px;bottom:10px;font-size:4px;line-height:1.5;color:var(--muted)}
.contact--right{left:auto;right:12px;text-align:right}
.brand.corner--low{top:56px}
.centered-brand{position:absolute;left:0;right:0;top:34px;justify-content:center;font-size:9px;color:var(--ink)}
.centered-brand .brand-dot{width:10px;height:10px}
</style>
</head>
<body>
<main class="canvas">
  <section class="letterhead letterhead--band">
    <header class="lh-band">
      <div class="brand"><span class="brand-dot"></span>Vantorix</div>
      <div class="lh-address">7153 Hollow Creek Brannock, Port Elsin VI 00947<br>Phone: 340.555.0182 Fax: 340.555.0183<br>sales@vantorix.net<br>vantorix.net</div>
    </header>
  </section>

  <section class="letterhead letterhead--centered">
    <header class="lh-center">
      <div class="brand"><span class="brand-dot"></span>Vantorix</div>
      <div class="lh-address">7153 Hollow Creek Brannock<br>Port Elsin VI 00947<br>Phone: 340.555.0182 Fax: 340.555.0183<br>sales@vantorix.net</div>
    </header>
  </section>

  <article class="card card--dark" style="left:763px;top:24px">
    <p class="tagline">Ultimate digital experience</p>
    <p class="card-mini">vantorix.net</p>
  </article>
  <article class="card card--dark" style="left:984px;top:24px">
    <div class="brand"><span class="brand-dot"></span>Vantorix</div>
  </article>

  <article class="card" style="left:763px;top:206px">
    <div class="top-gold"></div>
    <div class="brand corner"><span class="brand-dot"></span>Vantorix</div>
    <div class="person"><p class="person-name">Dalton Prewitt</p><p class="person-role">Owner</p></div>
    <p class="contact">7153 Hollow Creek Brannock, Port Elsin VI 00947<br>Phone: 340.555.0182 · sales@vantorix.net</p>
  </article>
  <article class="card" style="left:984px;top:206px">
    <div class="top-dark"></div>
    <div class="brand corner"><span class="brand-dot"></span>Vantorix</div>
    <div class="person"><p class="person-name person-name--ink">Dalton Prewitt</p><p class="person-role">Owner</p></div>
    <p class="contact">7153 Hollow Creek Brannock, Port Elsin VI 00947<br>Phone: 340.555.0182 · sales@vantorix.net</p>
  </article>

  <article class="card" style="left:763px;top:372px">
    <div class="brand corner corner--low"><span class="brand-dot"></span>Vantorix</div>
    <div class="person person--large"><p class="person-name">Dalton Prewitt</p><p class="person-role">Owner</p></div>
    <p class="contact contact--right">7153 Hollow Creek<br>Brannock, Port Elsin VI 00947<br>Phone: 340.555.0182<br>sales@vantorix.net</p>
  </article>
  <article class="card" style="left:984px;top:372px">
    <div class="brand centered-brand"><span class="brand-dot"></span>Vantorix</div>
    <div class="bottom-dark"></div>
  </article>
</main>
</body>
</html>
```